Wendel Sparkling Fruit boutique soft drinks need a label

Wendel sparkling fruit fizz is a range of non-alcoholic carbonated drinks flavoured with fruits grown on and around our farm in Richmond, southern Tasmania. The initial flavour will be raspberry, but there are more flavours to follow, lemon, cherry, strawberry. Our market will be local businesses, vineyards and overseas tourists who visit our farmstay accommodation and are looking for a classy 'up market' soft drink. Size will be around 360ml - stubby type bottles. Am open to all ideas, but probably looking for something with maximum 4? colours, reds and golds, rolling hills, farm/country feel with fresh fruits. Cool and inviting.
Target Market(s)
Vineyards, tourists, adults
Industry/Entity Type
Accommodation
Look and feel

```html
<!DOCTYPE html>
<html lang="en">
<head>
<meta charset="utf-8">
<title>Wendel Sparkling Fruit – Raspberry Label</title>
<link rel="stylesheet" href="https://fonts.googleapis.com/css2?family=Oswald:wght@500;700&display=swap">
<style>
  :root {
    --backdrop: #ececec;
    --paper: #f3ede2;
    --paper-edge: #e4dac8;
    --berry: #b3206f;
    --berry-dark: #8c1655;
    --leaf: #3f7a3a;
    --hills: #cdbf95;
    --hills-light: #e6dcc2;
    --white: #ffffff;
  }
  html, body {
    margin: 0;
    padding: 0;
    width: 821px;
    height: 1200px;
    overflow: hidden;
    background: var(--backdrop);
  }
  .canvas {
    position: relative;
    width: 821px;
    height: 1200px;
  }
  .label {
    position: absolute;
    left: 60px;
    top: 195px;
    width: 700px;
    height: 810px;
    box-shadow: 0 4px 18px rgba(0,0,0,0.12);
  }
  .label text {
    font-family: "Oswald", sans-serif;
  }
  .flavour { font-weight: 700; font-size: 44px; letter-spacing: 2px; fill: var(--berry); }
  .brand-name { font-weight: 700; font-size: 200px; fill: var(--berry); }
  .product-type { font-weight: 700; font-size: 36px; letter-spacing: 3px; fill: var(--white); }
  .tagline { font-weight: 500; font-size: 22px; letter-spacing: 1px; fill: var(--berry); }
  .volume { font-weight: 500; font-size: 16px; letter-spacing: 1px; fill: var(--berry); }
</style>
</head>
<body>
<main class="canvas">
  <svg class="label" viewBox="0 0 700 810" xmlns="http://www.w3.org/2000/svg">
    <defs>
      <radialGradient id="paper-tone" cx="50%" cy="45%" r="75%">
        <stop offset="0%" stop-color="#f7f2e9"/>
        <stop offset="100%" stop-color="#e6dcc9"/>
      </radialGradient>
      <linearGradient id="hills-tone" x1="0" y1="0" x2="0" y2="1">
        <stop offset="0%" stop-color="#eee6d2" stop-opacity="0"/>
        <stop offset="35%" stop-color="#ddd0ad"/>
        <stop offset="100%" stop-color="#cdbf95" stop-opacity="0.4"/>
      </linearGradient>
      <linearGradient id="berry-tone" x1="0" y1="0" x2="0" y2="1">
        <stop offset="0%" stop-color="#3f7a3a"/>
        <stop offset="30%" stop-color="#b3206f"/>
        <stop offset="100%" stop-color="#8c1655"/>
      </linearGradient>
    </defs>

    <rect class="label-paper" width="700" height="810" fill="url(#paper-tone)"/>

    <rect class="fruit-illustration" x="230" y="50" width="240" height="135" rx="60"
          fill="url(#berry-tone)" role="img" aria-label="Illustration of two raspberries with green leaves"/>

    <text class="flavour" x="350" y="226" text-anchor="middle">RASPBERRY</text>

    <rect class="landscape-illustration" x="20" y="245" width="660" height="300"
          fill="url(#hills-tone)" role="img" aria-label="Engraved-style sketch of rolling farm hills and fields"/>

    <text class="brand-name" x="350" y="640" text-anchor="middle"
          textLength="600" lengthAdjust="spacingAndGlyphs">WENDEL'S</text>

    <g class="product-ribbon">
      <polygon points="95,668 140,668 140,716 95,716 112,692" fill="var(--berry-dark)"/>
      <polygon points="605,668 560,668 560,716 605,716 588,692" fill="var(--berry-dark)"/>
      <rect x="125" y="662" width="450" height="50" fill="var(--berry)"/>
      <text class="product-type" x="350" y="701" text-anchor="middle">SPARKLING JUICE</text>
    </g>

    <text class="tagline" x="350" y="748" text-anchor="middle">MADE FROM LOCALLY GROWN PRODUCE</text>
    <text class="volume" x="665" y="778" text-anchor="end">350 ML</text>
  </svg>
</main>
</body>
</html>
```